Cosmetic Surgery Ad for a magazine

We would like design options for our cosmetic surgery practice located in California for summer advertizing breast augmentation and liposuction to get ready for a beach body.

Target Market(s)

Women ages 25 - 40

Industry/Entity Type

Cosmetic

Other font styles liked:
• see brand standards attachment

Requirements
Must have
• Our logo (see brand standards attachment)
Should not have
• Nudity

```html
<!DOCTYPE html>
<html lang="en">
<head>
<meta charset="utf-8">
<title>Beach Body Ad – Belle Contour</title>
<link rel="stylesheet" href="https://fonts.googleapis.com/css2?family=Roboto+Condensed:wght@400;700&family=Arimo:wght@400&display=swap">
<style>
  :root {
    --backdrop: #ece8e2;
    --page: #ffffff;
    --pink: #f08aa6;
    --pink-soft: #f2a7b8;
    --green: #8dcf88;
    --ink: #1d1d1d;
    --sky-top: #b9d3e6;
    --sky-mid: #e6edf1;
    --sand: #e4d8cd;
    --warm: #e7b79f;
  }
  * { margin: 0; padding: 0; box-sizing: border-box; }
  html, body { width: 1200px; height: 795px; overflow: hidden; background: var(--backdrop); }
  .ad-page {
    position: absolute;
    left: 300px; top: 18px;
    width: 600px; height: 760px;
    background: var(--page);
    box-shadow: 0 4px 18px rgba(0,0,0,.15);
    overflow: hidden;
  }
  .hero-photo {
    position: absolute; left: 0; top: 0;
    width: 600px; height: 400px;
    background: linear-gradient(100deg, var(--sky-top) 0%, var(--sky-mid) 40%, var(--sand) 70%, var(--warm) 100%);
  }
  .headline {
    position: absolute; left: 48px; top: 418px;
    font-family: "Roboto Condensed", sans-serif;
    font-weight: 400;
    line-height: 1;
  }
  .headline .lead { display: block; color: var(--pink-soft); font-size: 46px; }
  .headline .lead-line { display: block; margin-top: 2px; }
  .headline .small { color: var(--pink-soft); font-size: 46px; }
  .headline .big { color: var(--green); font-size: 62px; font-weight: 700; margin-left: 10px; }
  .body-copy {
    position: absolute; left: 48px; top: 548px;
    width: 490px;
    font-family: "Arimo", sans-serif;
    font-size: 12.5px; line-height: 1.3;
    color: var(--ink);
    text-align: justify;
  }
  .rule {
    position: absolute; left: 0; top: 738px;
    width: 360px; height: 2px;
    background: var(--pink);
  }
  .brand {
    position: absolute; right: 24px; top: 692px;
    font-family: "Roboto Condensed", sans-serif;
  }
  .brand .name { display: block; color: var(--green); font-size: 38px; font-weight: 400; line-height: 1; }
  .brand .tagline { display: block; color: var(--pink); font-size: 11px; letter-spacing: .3px; margin-top: 3px; }
</style>
</head>
<body>
  <main class="ad-page">
    <div class="hero-photo" role="img" aria-label="Photo of a woman in a pink bikini measuring her waist with a tape measure on a sunny beach"></div>
    <h1 class="headline">
      <span class="lead">Get ready</span>
      <span class="lead-line"><span class="small">for a</span><span class="big">Beach Body</span></span>
    </h1>
    <p class="body-copy">As one of the most popular cosmetic procedures we deliver, breast augmentation at Belle Contour in Bakersfield is done to achieve natural, comfortable results in an environment that promotes healing and betterment. We approach each surgery by first listening to the patient, ensuring a total understanding is reached before continuing. Our patients report total satisfaction after their procedures, calling it the finest breast augmentation Bakersfield has available.</p>
    <div class="rule"></div>
    <div class="brand">
      <span class="name">Belle Contour</span>
      <span class="tagline">COSMETIC SURGERY AND MEDSPA</span>
    </div>
  </main>
</body>
</html>
```